Bright-Ladder Brochure

We would like a 3 panel layout format with copy on both sides and on each panel, (we will provide content).

We are Bright-Ladder and we work with business owners to achieve measurable growth and success based on 5 Core Pillars Of Momentum and (S.W.E) 60 Week Steady Whole Endeavour. We also work with the business leader and individuals within the organization with personal development.

We would like the brochure to have a corporate feel, but warm and inviting. We don't want a hard or aggressive feel.

We would like it to be available for pdf upload and physical print formats.

The winning design will also be invited to design a header for our website as well. The header will be consistent with the brochure, so please keep that in mind during your creative process.

I am enclosing a transparent copy of our company logo along with content for the brochure.

Thank you in advance for your consideration!

Gordon and Lorna
Updates

Sorry, but we forgot to include the front cover text.

It will read as follows,

Do you know the 5 Core Pillars Of Momentum  that are crucial to the success of any business today?

Also, please add the following to the back page

Website: www.bright-ladder-example.com
Resource Centre: www.blhubfiles-example.com 
Phone: +44 (0) 7700900417
Email: info@bright-ladder-example.com

Follow us on (please insert Facebook, Linkedin and YouTube logo)

I have uploaded a pdf format of brochure text.

Hello designers. I wanted to give some further input to help the process. Although the brochure is to target business, we don't want to over do it with corporate professioanls in all the photos. If there is an opportunity to incorporate photos of small business owners like, a butcher, baker, chef, flower shop etc. This would hopefully help us make an immpression to all small business owners.

Thank you, and good luck!

Gordon and Lorna  

Reason: A few designers have come come on board last minute. So I'd like to give everyone the same opportunity to respond. Sincerely, Gordon

Target Market(s)

Small Business Owners searching for new ways to grow their business in the UK and Republic Of Ireland.

Industry/Entity Type

Business

```html
<!DOCTYPE html>
<html lang="en">
<head>
<meta charset="utf-8">
<title>Bright-Ladder Brochure – Inside Spread</title>
<link rel="stylesheet" href="https://fonts.googleapis.com/css2?family=Carlito:wght@400;700&family=Oswald:wght@500;700&display=swap">
<style>
  :root {
    --page-bg: #e8e7ea;
    --panel-white: #fdfbfd;
    --panel-mist: #ebe7ed;
    --band: rgba(196, 150, 205, 0.22);
    --band-soft: rgba(214, 180, 222, 0.16);
    --plum: #6d2d72;
    --plum-deep: #4a1750;
    --plum-fold: #32103a;
    --ink: #5c2a63;
    --quote-grey: #6f6f74;
    --quote-accent: #7a2f80;
    --card: #f1eff2;
  }
  * { box-sizing: border-box; margin: 0; padding: 0; }
  html, body {
    width: 1200px; height: 851px; overflow: hidden;
    background: var(--page-bg);
  }
  body { position: relative; font-family: "Carlito", "Calibri", sans-serif; color: var(--ink); }

  .brochure {
    position: absolute; left: 90px; top: 55px;
    width: 1020px; height: 740px;
    display: flex;
    box-shadow: 0 6px 24px rgba(0,0,0,0.12);
  }
  .panel {
    position: relative; width: 340px; height: 100%;
    background:
      linear-gradient(163deg, transparent 14%, var(--band) 15.5%, transparent 21%),
      linear-gradient(163deg, transparent 24%, var(--band-soft) 26%, transparent 31%),
      linear-gradient(158deg, transparent 74%, var(--band) 76%, transparent 81%),
      linear-gradient(158deg, transparent 84%, var(--band-soft) 86%, transparent 92%),
      var(--panel-white);
  }
  .panel--centre {
    background:
      linear-gradient(163deg, transparent 30%, rgba(255,255,255,0.5) 33%, transparent 40%),
      var(--panel-mist);
  }

  .ribbon {
    position: absolute; height: 42px;
    background: linear-gradient(180deg, #83408a 0%, var(--plum) 45%, var(--plum-deep) 100%);
    color: #fff; font-size: 17px;
    display: flex; align-items: center; justify-content: center;
  }
  .ribbon::before {
    content: ""; position: absolute; left: 0; bottom: -11px;
    border-top: 11px solid var(--plum-fold);
    border-left: 14px solid transparent;
  }
  .ribbon::after {
    content: ""; position: absolute; right: 0; top: -11px;
    border-bottom: 11px solid var(--plum-fold);
    border-right: 14px solid transparent;
  }
  .ribbon--small { height: 32px; font-size: 15px; }

  .copy {
    position: absolute; font-size: 15px; line-height: 1.45;
    text-align: justify;
  }
  .copy p { text-indent: 3em; }
  .copy p + p { margin-top: 18px; }

  /* Left panel */
  .ribbon--economy { left: 68px; top: 48px; width: 214px; }
  .copy--economy { left: 28px; right: 22px; top: 118px; }
  .illustration {
    position: absolute; left: 40px; top: 470px; width: 260px; height: 220px;
    border-radius: 4px;
    background:
      radial-gradient(circle at 52% 20%, #c9c4d2 0 18%, transparent 19%),
      linear-gradient(180deg, transparent 30%, #2c2a30 30%, #3a383f 78%, rgba(255,255,255,0) 100%);
    opacity: 0.85;
  }

  /* Centre panel */
  .quote-card {
    position: absolute; left: 22px; top: 40px; width: 300px; height: 140px;
    background: var(--card);
    transform: rotate(-8deg);
    box-shadow: 0 4px 10px rgba(0,0,0,0.12);
    display: flex; align-items: center; justify-content: center;
  }
  .quote-card__text {
    font-family: "Oswald", "Arial Narrow", sans-serif; font-weight: 700;
    font-size: 24px; line-height: 1.15; text-align: center;
    color: var(--quote-grey);
  }
  .quote-card__text strong { color: var(--quote-accent); font-weight: 700; }
  .ribbon--helping { left: 62px; top: 215px; width: 218px; }
  .copy--helping { left: 22px; right: 22px; top: 280px; }

  /* Right panel */
  .ribbon--solutions { left: 52px; top: 56px; width: 220px; }
  .copy--solutions { left: 22px; right: 26px; top: 122px; }
  .services {
    list-style: none; margin-top: 14px; text-align: left;
  }
  .services li { position: relative; padding-left: 26px; }
  .services li::before {
    content: ""; position: absolute; left: 4px; top: 7px;
    width: 6px; height: 6px;
    border-right: 2px solid var(--plum-deep); border-top: 2px solid var(--plum-deep);
    transform: rotate(45deg);
  }
  .ribbon--resource { left: 52px; top: 410px; width: 220px; }
  .copy--resource { left: 22px; right: 26px; top: 475px; }
  .ribbon--url { left: 50px; top: 545px; width: 214px; }
  .copy--access { left: 22px; right: 26px; top: 597px; }
</style>
</head>
<body>
  <main class="brochure" aria-label="Bright-Ladder brochure inside spread">
    <section class="panel panel--left">
      <h2 class="ribbon ribbon--economy">The New Economy</h2>
      <div class="copy copy--economy">
        <p>The economy is finally beginning to show signs of recovery. You may not realize that small to medium businesses generate half of the U.K’s national income and two thirds of all employment, so undoubtedly they are playing a major role in this “new economy” that is emerging.</p>
        <p>Business is changing fast and it is more competitive than ever, so it is vital to the success of any company, to find innovative and creative ways to attract new customers keep them coming back and stay ahead of the competition.</p>
      </div>
      <div class="illustration" role="img" aria-label="Illustration of a group of business people in silhouette standing in front of a globe"></div>
    </section>

    <section class="panel panel--centre">
      <div class="quote-card">
        <p class="quote-card__text">"...zero to over <strong>6 MILLION</strong> in<br>revenues <strong>in</strong> just under 2<br>years!"</p>
      </div>
      <h2 class="ribbon ribbon--helping">Helping your Business!</h2>
      <div class="copy copy--helping">
        <p>Recently there has been a growing trend in small business owners enlisting outside sources to help them find ways to grow and promote their businesses. At Bright-Ladder we have over 30 years combined experience in management, ownership and consulting in a wide array of businesses. We know what works and what doesn’t, and being entrepreneurs ourselves, we know firsthand the struggles that can come with owning a business.</p>
        <p>Our latest venture saw us grow a new construction company from 0 to over 6 MILLION in revenues in just under 2 years. This was achieved through the implementation of our unique sales, marketing and customer service strategies. Our genuine desire to help businesses and individuals succeed is what Bright-Ladder is all about.</p>
      </div>
    </section>

    <section class="panel panel--right">
      <h2 class="ribbon ribbon--solutions">Business Solutions</h2>
      <div class="copy copy--solutions">
        <p>In addition to the Total Business Analysis / S.W.E package, we also offer other business solutions which can be used individually or bundled together to create a package suitable for your needs.</p>
        <ul class="services">
          <li>One on one business mentoring</li>
          <li>Marketing strategies</li>
          <li>Sales training. (individual or group)</li>
          <li>Management training. (individual or group)</li>
          <li>Customer service training. (individual or group)</li>
        </ul>
      </div>
      <h2 class="ribbon ribbon--resource">Resource Centre</h2>
      <div class="copy copy--resource">
        <p>At Bright-Ladder, we are dedicated to providing current and relevant information through our resource centre:</p>
      </div>
      <p class="ribbon ribbon--small ribbon--url">www.blhubfiles-example.com</p>
      <div class="copy copy--access">
        <p>Where you will find access to videos, reports, statistics and newsletters. You will also find details on upcoming events, such as webinars, workshops and online training.</p>
      </div>
    </section>
  </main>
</body>
</html>
```